Fresh Produce Outlet needs a Poster Design

Hi,
We are Brightleaf Harvest Market, a fruit and veg outlet based in the suburb of Yanchep, Perth, Western Australia.Apart from fresh produce, we also stock nuts and grains, organic products and specialty grocery. We are about to launch a re-branding exercise, projecting ourselves as 'the' shop for fresh produce; quality, taste and freshness being our key differentiators. We are competing against a big supermarket chain who are using marketing muscle power to shut us down and we want to respond with a series of posters which are simple yet bold and sends a clear and positive message to our customers about what we have to offer.
Please feel free to visit our Facebook page www.facebook.com/brightleafharvestmkt to get an idea about our current branding,logo and the shop in general.
Regards
Team - Brightleaf Harvest Market
Target Market(s)
Residents of Yanchep and surrounding suburbs
Industry/Entity Type
Retail
Look and feel

```html
<!DOCTYPE html>
<html lang="en">
<head>
<meta charset="utf-8">
<title>Brightleaf Harvest Market – Quality Taste Freshness</title>
<link href="https://fonts.googleapis.com/css2?family=Montserrat:wght@600&family=Open+Sans:ital,wght@0,400;0,500;1,700&display=swap" rel="stylesheet">
<style>
  :root {
    --paper: #f1f6ea;
    --quality-red: #a42b36;
    --taste-orange: #f2891c;
    --fresh-green: #5e9b2f;
    --brand-green: #24531c;
    --tag-orange: #f09a3c;
    --leaf-light: #a6dc3e;
    --leaf-dark: #2f6a19;
    --berry-dark: #962052;
    --berry-bright: #e5174a;
  }
  html, body {
    margin: 0;
    padding: 0;
    overflow: hidden;
  }
  body {
    width: 849px;
    height: 1200px;
    background: #ffffff;
  }
  .poster {
    position: relative;
    width: 849px;
    height: 1200px;
    overflow: hidden;
    background: #ffffff;
  }
  .poster__shapes {
    position: absolute;
    inset: 0;
  }
  .headline {
    position: absolute;
    left: 0;
    right: 0;
    margin: 0;
    text-align: center;
    font-family: "Montserrat", sans-serif;
    font-weight: 600;
    line-height: 1;
    letter-spacing: 1px;
  }
  .headline--quality {
    top: 446px;
    font-size: 128px;
    color: var(--quality-red);
  }
  .headline--taste {
    top: 566px;
    font-size: 128px;
    color: var(--taste-orange);
  }
  .headline--freshness {
    top: 688px;
    font-size: 128px;
    color: var(--fresh-green);
  }
  .brand {
    position: absolute;
    top: 1038px;
    left: 0;
    right: 0;
    margin: 0;
    text-align: center;
    font-family: "Open Sans", sans-serif;
    font-weight: 500;
    font-size: 52px;
    color: var(--brand-green);
    letter-spacing: -0.5px;
  }
  .tagline {
    position: absolute;
    top: 1112px;
    left: 0;
    right: 0;
    margin: 0;
    text-align: center;
    font-family: "Open Sans", sans-serif;
    font-weight: 400;
    font-size: 38px;
    color: var(--tag-orange);
  }
  .tagline__place {
    font-weight: 700;
    font-style: italic;
  }
</style>
</head>
<body>
  <main class="poster">
    <svg class="poster__shapes" width="849" height="1200" viewBox="0 0 849 1200" aria-hidden="false">
      <defs>
        <radialGradient id="produceTones" cx="50%" cy="40%" r="70%">
          <stop offset="0%" stop-color="#f4a23c"/>
          <stop offset="45%" stop-color="#e0562e"/>
          <stop offset="80%" stop-color="#6f9d34"/>
          <stop offset="100%" stop-color="#ffffff"/>
        </radialGradient>
        <linearGradient id="leafBand" x1="0" y1="0" x2="1" y2="0">
          <stop offset="0%" stop-color="var(--leaf-light)"/>
          <stop offset="55%" stop-color="#8ccb32"/>
          <stop offset="100%" stop-color="var(--leaf-dark)"/>
        </linearGradient>
        <linearGradient id="berryBand" x1="0" y1="0" x2="1" y2="0">
          <stop offset="0%" stop-color="var(--berry-dark)"/>
          <stop offset="40%" stop-color="#d21a4b"/>
          <stop offset="100%" stop-color="var(--berry-bright)"/>
        </linearGradient>
      </defs>

      <rect class="produce-photo" x="0" y="0" width="849" height="420" fill="url(#produceTones)" role="img" aria-label="Photograph of fresh fruit and vegetables: carrots, kale, tomatoes, melon, a glass of juice, bananas, pineapple, oranges, mango, apples and grapes"/>

      <path class="leaf-swoosh" d="M0,388 C260,408 520,370 640,318 C720,288 790,284 849,290 L849,460 L0,460 Z" fill="url(#leafBand)"/>

      <path class="paper" d="M0,406 C280,418 560,392 700,398 C770,402 815,418 849,440 L849,1200 L0,1200 Z" fill="var(--paper)"/>

      <path class="berry-swoosh" d="M0,885 C230,858 440,890 620,955 C720,990 790,1016 849,1022 L849,1028 C780,1020 700,1000 610,978 C440,940 240,942 0,968 Z" fill="url(#berryBand)"/>
    </svg>

    <h1 class="headline headline--quality">QUALITY</h1>
    <p class="headline headline--taste">TASTE</p>
    <p class="headline headline--freshness">FRESHNESS</p>

    <p class="brand">Brightleaf Harvest Market</p>
    <p class="tagline">the shop for fresh produce in <span class="tagline__place">Yanchep</span></p>
  </main>
</body>
</html>
```